I need to add on from our previous project a couple extra signs

We need to create two signs from your original desgin with a arrow saying 600M on the left.
also another sign drawn up similar to the one attached but also adding in there that the containers are 20ft/40ft and we have caravan, car and boat storage.
also add on the sign something for " sign online or call the number to rent space"

```html
<!DOCTYPE html>
<html lang="en">
<head>
<meta charset="utf-8">
<title>Keyline Storage – Road Signs</title>
<link rel="stylesheet" href="https://fonts.googleapis.com/css2?family=Archivo:wdth,wght@125,800;125,900&family=Poppins:wght@400;600;700;800&display=swap">
<style>
  :root {
    --red: #cc1f27;
    --ink: #2a2728;
    --white: #ffffff;
    --backdrop: #d3d3d3;
    --divider: #e2e2e2;
  }
  html, body {
    margin: 0;
    width: 1200px;
    height: 932px;
    overflow: hidden;
    background: var(--backdrop);
  }
  .sign {
    position: absolute;
    display: block;
    background: var(--white);
  }
  .sign--distance { left: 273px; top: 113px; width: 655px; height: 325px; }
  .sign--info { left: 78px; top: 491px; width: 1040px; height: 303px; }
  .display { font-family: "Archivo", sans-serif; font-stretch: 125%; font-weight: 900; }
  .body { font-family: "Poppins", sans-serif; }
  .brand-name { font-family: "Poppins", sans-serif; font-weight: 700; fill: var(--ink); }
  .brand-url { font-family: "Poppins", sans-serif; font-weight: 400; fill: var(--ink); }
  .brand-phone { font-family: "Archivo", sans-serif; font-stretch: 125%; font-weight: 800; fill: var(--red); }
  .fill-red { fill: var(--red); }
  .fill-ink { fill: var(--ink); }
  .fill-white { fill: var(--white); }
</style>
</head>
<body>

<!-- Directional sign -->
<svg class="sign sign--distance" viewBox="0 0 655 325" role="img" aria-label="Keyline Storage 600 metres on left">
  <defs>
    <clipPath id="arc-top"><rect x="0" y="0" width="655" height="142"/></clipPath>
    <clipPath id="arc-bottom"><rect x="0" y="223" width="655" height="102"/></clipPath>
    <clipPath id="sign-bounds"><rect x="0" y="0" width="655" height="325"/></clipPath>
  </defs>
  <g clip-path="url(#sign-bounds)">
    <circle cx="115" cy="140" r="239" fill="none" stroke="var(--red)" stroke-width="30" clip-path="url(#arc-top)"/>
    <circle cx="115" cy="140" r="239" fill="none" stroke="var(--ink)" stroke-width="30" clip-path="url(#arc-bottom)"/>
  </g>

  <text class="display" x="42" y="142" font-size="66" textLength="278" lengthAdjust="spacingAndGlyphs"><tspan class="fill-red">600</tspan><tspan class="fill-ink">m</tspan></text>
  <text class="display" x="42" y="247" font-size="33" textLength="190" lengthAdjust="spacingAndGlyphs"><tspan class="fill-ink">ON </tspan><tspan class="fill-red">LEFT</tspan></text>

  <g class="brand">
    <circle cx="395" cy="184" r="29" class="fill-red"/>
    <text class="brand-name" x="432" y="166" font-size="21" textLength="130" lengthAdjust="spacingAndGlyphs">KEYLINE</text>
    <text class="brand-name" x="432" y="190" font-size="21" textLength="130" lengthAdjust="spacingAndGlyphs">STORAGE</text>
    <text class="brand-url" x="432" y="204" font-size="8.5" textLength="126" lengthAdjust="spacingAndGlyphs">www.keylinestorage.com.au</text>
    <text class="brand-phone" x="432" y="216" font-size="9.5" textLength="126" lengthAdjust="spacingAndGlyphs">(03) 5550 0142</text>
  </g>

  <g class="arrow">
    <polygon points="592,16 625,61 559,61" class="fill-red"/>
    <polygon points="592,30 621,79 562,79" class="fill-ink"/>
    <rect x="577" y="78" width="30" height="247" class="fill-ink"/>
  </g>
</svg>

<!-- Information sign -->
<svg class="sign sign--info" viewBox="0 0 1040 303" role="img" aria-label="Keyline Storage information sign">
  <path class="fill-red" d="M354,0 L405,0 Q453,62 453,137 L414,137 Q410,58 354,0 Z"/>
  <path class="fill-ink" d="M0,161 L453,161 Q447,240 402,303 L0,303 Z"/>

  <g class="brand">
    <circle cx="83" cy="68" r="27" class="fill-red"/>
    <text class="brand-name" x="115" y="54" font-size="20" textLength="116" lengthAdjust="spacingAndGlyphs">KEYLINE</text>
    <text class="brand-name" x="115" y="76" font-size="20" textLength="116" lengthAdjust="spacingAndGlyphs">STORAGE</text>
    <text class="brand-url" x="115" y="88" font-size="8" textLength="114" lengthAdjust="spacingAndGlyphs">www.keylinestorage.com.au</text>
    <text class="brand-phone" x="115" y="99" font-size="9" textLength="114" lengthAdjust="spacingAndGlyphs">(03) 5550 0142</text>
  </g>

  <text class="display" x="60" y="137" font-size="29" textLength="322" lengthAdjust="spacingAndGlyphs"><tspan class="fill-red">WHY CHOOSE </tspan><tspan class="fill-ink">US?</tspan></text>

  <text class="body fill-white" x="59" y="215" font-size="23" font-weight="400" textLength="260" lengthAdjust="spacingAndGlyphs">OUR CONTAINERS ARE</text>
  <text class="display fill-white" x="59" y="259" font-size="42" textLength="311" lengthAdjust="spacingAndGlyphs">20FT/40FT</text>

  <g class="availability">
    <text class="body fill-red" x="489" y="52" font-size="26" font-weight="800" textLength="270" lengthAdjust="spacingAndGlyphs">CHECK ONLINE FOR</text>
    <text class="body fill-red" x="489" y="86" font-size="39" font-weight="800" textLength="270" lengthAdjust="spacingAndGlyphs">AVAILABILITY</text>
    <text class="body fill-ink" x="489" y="109" font-size="25" font-weight="400" textLength="270" lengthAdjust="spacingAndGlyphs">OR CALL THIS NUMBER</text>
    <path class="fill-red" transform="translate(489,121) scale(1.05)" d="M6.62 10.79c1.44 2.83 3.76 5.14 6.59 6.59l2.2-2.2c.27-.27.67-.36 1.02-.24 1.120.37 2.33.57 3.57.57.55 0 1 .45 1 1V20c0 .55-.45 1-1 1-9.39 0-17-7.61-17-17 0-.55.45-1 1-1h3.5c.55 0 1 .45 1 1 0 1.25.2 2.45.57 3.57.11.35.03.74-.25 1.02l-2.2 2.2z"/>
    <text class="body fill-ink" x="519" y="143" font-size="30" font-weight="700" textLength="241" lengthAdjust="spacingAndGlyphs">(03) 5550 0141</text>
  </g>

  <g class="also-have">
    <path class="fill-red" d="M792,0 H980 V122 Q980,142 960,142 H812 Q792,142 792,122 Z"/>
    <text class="body fill-white" x="813" y="46" font-size="19" font-weight="800" textLength="147" lengthAdjust="spacingAndGlyphs">WE ALSO HAVE</text>
    <g class="check-item">
      <rect x="813" y="58" width="14" height="14" rx="3" class="fill-white"/>
      <path d="M815,64 L819,69 L828,57" fill="none" stroke="var(--ink)" stroke-width="2.6" stroke-linecap="round"/>
      <text class="body fill-white" x="836" y="71" font-size="18" font-weight="600">Caravan</text>
    </g>
    <g class="check-item">
      <rect x="813" y="82" width="14" height="14" rx="3" class="fill-white"/>
      <path d="M815,88 L819,93 L828,81" fill="none" stroke="var(--ink)" stroke-width="2.6" stroke-linecap="round"/>
      <text class="body fill-white" x="836" y="95" font-size="18" font-weight="600">Car</text>
    </g>
    <g class="check-item">
      <rect x="813" y="106" width="14" height="14" rx="3" class="fill-white"/>
      <path d="M815,112 L819,117 L828,105" fill="none" stroke="var(--ink)" stroke-width="2.6" stroke-linecap="round"/>
      <text class="body fill-white" x="836" y="119" font-size="18" font-weight="600" textLength="112" lengthAdjust="spacingAndGlyphs">Boat storage</text>
    </g>
  </g>

  <g class="free-from">
    <text class="body fill-ink" x="489" y="190" font-size="19" font-weight="700" textLength="393" lengthAdjust="spacingAndGlyphs">SHIPPING CONTAINERS ARE FREE FROM</text>
    <path d="M888,175 H963 Q978,175 978,190 V241" fill="none" stroke="var(--red)" stroke-width="1.5"/>

    <line x1="604" y1="200" x2="604" y2="280" stroke="var(--divider)" stroke-width="1.5"/>
    <line x1="743" y1="200" x2="743" y2="280" stroke="var(--divider)" stroke-width="1.5"/>
    <line x1="880" y1="200" x2="880" y2="280" stroke="var(--divider)" stroke-width="1.5"/>

    <rect x="518" y="206" width="34" height="34" rx="6" class="fill-red" role="img" aria-label="Vermin icon"/>
    <rect x="656" y="206" width="34" height="34" rx="6" class="fill-red" role="img" aria-label="Insect icon"/>
    <rect x="795" y="206" width="34" height="34" rx="6" class="fill-red" role="img" aria-label="Water drops icon"/>
    <rect x="918" y="206" width="34" height="34" rx="6" class="fill-red" role="img" aria-label="Dust cloud icon"/>

    <text class="body fill-ink" x="535" y="268" font-size="24" font-weight="700" text-anchor="middle">VERMIN</text>
    <text class="body fill-ink" x="673" y="268" font-size="24" font-weight="700" text-anchor="middle">INSECT</text>
    <text class="body fill-ink" x="812" y="268" font-size="24" font-weight="700" text-anchor="middle">WATER</text>
    <text class="body fill-ink" x="935" y="268" font-size="24" font-weight="700" text-anchor="middle">DUST</text>
  </g>
</svg>

</body>
</html>
```